Career Counselor in need of a business card design

Hello Creatives! I'm in need of a business card design for a new company based in Georgia, USA called Pathways By Lumen.

Some things that may be helpful in creating your concept(s) include:

My Logo (Included in the Files section): There are three versions, two versions are in the second file. The all gold stacked (vertical) version is my primary logo and then there are two horizontal versions (one is all gold and the other is gold and grey).

My mission: to empower tweens through young adults to realize and actualize their CAREER ASPIRATIONS.
My vision: for tweens through young adults to LIVE LIFE ON PURPOSE and become CONTRIBUTING MEMBERS OF SOCIETY.

Biblical scriptures that support my ‘Why’: Psalms 127: 3-4(NIV) Children are a heritage from the Lord, offspring a reward from him. Like ARROWS in the hands of a warrior are children…. And Proverbs 29:18(JKV) Where there is no VISION, the people perish.

*Words in ALL CAPS are to emphasize what's important to me and may possibly provide you some inspiration (IDK - Have fun with it)!

Target Market(s)

My ideal customers are parents, guardians, and young adults.

Contact Information for Business Card

My name, degrees and credential: Delmira Fosket, M.S., Ed.S., NCC
Title: College and Career Coach and Consultant

Number: 555.317.8842
Address: 2618 Velbrook Avenue., Suite 407, Macon, GA 31299
Email: info@pathwaysbylumen.co
Website: www.pathwaysbylumen.co

My population: TWEENS • TEENS • EMERGING ADULTS
Services offered: One-On-One Sessions • Small Groups • Workshops

Colors

Designer to choose colors to be used in the design.

Requirements
Nice to have
• Either my mission or vision but I will understand if it does not all fit.
• My mission: To empower tweens through young adults to realize and actualize their career aspirations.
• My vision: For tweens through young adults to live life on purpose and become contributing members of society.

```html
<!DOCTYPE html>
<html lang="en">
<head>
<meta charset="utf-8">
<title>Pathways By Lumen – Business Card</title>
<link rel="stylesheet" href="https://fonts.googleapis.com/css2?family=Cinzel:wght@400;600&family=Tinos:wght@400;700&display=swap">
<style>
  :root{
    --stage:#2a2b2e;
    --card:#1d1f21;
    --card-edge:#151617;
    --gold:#d4a72c;
    --gold-light:#f1d06a;
    --gold-deep:#a87a14;
    --grey:#b9b9b9;
    --grey-dim:#8d8d8d;
    --ghost:#2a2c2f;
  }
  *{box-sizing:border-box;margin:0;padding:0}
  html,body{width:1200px;height:800px;overflow:hidden;background:var(--stage)}
  .stage{position:relative;width:1200px;height:800px}
  .card{
    position:absolute;width:540px;height:309px;background:var(--card);
    border-radius:4px;overflow:hidden;
    box-shadow:0 18px 40px rgba(0,0,0,.45);
    font-family:"Tinos",serif;
  }
  .card--front{left:40px;top:140px}
  .card--back{left:620px;top:350px}

  /* brand wordmark */
  .wordmark{font-family:"Cinzel",serif;color:var(--gold);display:flex;flex-direction:column;align-items:flex-start;line-height:1}
  .wordmark__main{font-size:46px;font-weight:600;letter-spacing:1px}
  .wordmark__sub{font-size:15px;letter-spacing:8px;margin-top:4px;color:var(--gold)}

  /* front */
  .front__brand{position:absolute;left:0;right:0;top:58px;display:flex;justify-content:center;align-items:center;gap:16px}
  .brand-dot{width:44px;height:44px;border-radius:50%;border:3px solid var(--gold)}
  .front__rule{position:absolute;left:50px;right:50px;height:1px;background:var(--gold)}
  .front__rule--top{top:168px}
  .front__rule--bottom{top:250px}
  .front__audience,.front__services{position:absolute;left:0;right:0;text-align:center;color:var(--grey)}
  .front__audience{top:184px;font-size:14px;letter-spacing:2px}
  .front__services{top:214px;font-size:15px;letter-spacing:1px}

  /* back */
  .back__ghost{position:absolute;right:-40px;top:-50px;width:260px;height:260px;border-radius:50%;border:28px solid var(--ghost)}
  .back__band{position:absolute;left:0;top:195px;width:72px;height:60px;background:linear-gradient(120deg,var(--gold-deep),var(--gold-light) 55%,var(--gold))}
  .back__dot{position:absolute;left:44px;top:183px;width:84px;height:84px;border-radius:50%;border:4px solid var(--gold);background:var(--card)}
  .back__divider{position:absolute;left:148px;top:70px;width:1px;height:70px;background:var(--gold)}
  .back__brand{position:absolute;left:162px;top:74px}
  .back__brand .wordmark__main{font-size:40px}
  .back__brand .wordmark__sub{color:var(--grey-dim);font-size:14px}
  .back__rule{position:absolute;left:150px;right:30px;top:190px;height:1px;background:var(--gold)}
  .person{position:absolute;left:150px;top:150px}
  .person__name{color:var(--gold);font-size:19px;font-weight:700}
  .person__title{color:var(--grey);font-size:13px;margin-top:2px}
  .contacts{position:absolute;left:150px;top:204px;list-style:none;color:var(--grey);font-size:12.5px}
  .contacts li{display:flex;align-items:center;gap:8px;margin-bottom:6px}
  .contacts svg{width:16px;height:16px;flex:none}
  .address{position:absolute;right:30px;top:120px;text-align:right;color:var(--grey);font-size:12.5px;line-height:1.5}
</style>
</head>
<body>
<main class="stage">

  <section class="card card--front" aria-label="Card front">
    <div class="front__brand">
      <span class="brand-dot"></span>
      <div class="wordmark">
        <span class="wordmark__main">PATHWAYS</span>
        <span class="wordmark__sub">BY LUMEN</span>
      </div>
    </div>
    <div class="front__rule front__rule--top"></div>
    <p class="front__audience">TWEENS • TEENS • EMERGING ADULTS</p>
    <p class="front__services">One-On-One Sessions • Small Groups • Workshops</p>
    <div class="front__rule front__rule--bottom"></div>
  </section>

  <section class="card card--back" aria-label="Card back">
    <div class="back__ghost"></div>
    <div class="back__band"></div>
    <span class="back__dot"></span>
    <div class="back__divider"></div>
    <div class="back__brand wordmark">
      <span class="wordmark__main">PATHWAYS</span>
      <span class="wordmark__sub">BY LUMEN</span>
    </div>
    <p class="address">2618 Velbrook Avenue.<br>Suite 407, Macon, GA 31299</p>
    <div class="person">
      <p class="person__name">Delmira Fosket, M.S., Ed.S., NCC</p>
      <p class="person__title">College and Career Coach and Consultant</p>
    </div>
    <div class="back__rule"></div>
    <ul class="contacts">
      <li><svg viewBox="0 0 16 16"><circle cx="8" cy="8" r="7" fill="none" stroke="#d4a72c"/><rect x="5.5" y="4" width="5" height="8" rx="1" fill="none" stroke="#d4a72c"/></svg>555.317.8842</li>
      <li><svg viewBox="0 0 16 16"><circle cx="8" cy="8" r="7" fill="none" stroke="#d4a72c"/><rect x="4.5" y="5.5" width="7" height="5" fill="none" stroke="#d4a72c"/><path d="M4.5 5.5 8 8.5 11.5 5.5" fill="none" stroke="#d4a72c"/></svg>info@pathwaysbylumen.co</li>
      <li><svg viewBox="0 0 16 16"><circle cx="8" cy="8" r="7" fill="none" stroke="#d4a72c"/><circle cx="8" cy="8" r="4" fill="none" stroke="#d4a72c"/><path d="M4 8h8M8 4v8" stroke="#d4a72c"/></svg>www.pathwaysbylumen.co</li>
    </ul>
  </section>

</main>
</body>
</html>
```